Post Card Design Bright Lantern Youth

We need a postcard design that will be mailed to all residents offering free pickups of donated clothing. Our foundation is called Bright Lantern Youth, we are a nonprofit charitable organization that provides meals and medical services to children in need in Honduras. Collecting unwanted second-hand clothing generates revenue that helps fund the mission and programs run by our foundation. We would like to offer our pickup services to everyone who has any unwanted reusable clothing.

```html
<!DOCTYPE html>
<html lang="en">
<head>
<meta charset="utf-8">
<title>Bright Lantern Youth – Clothing Donation Postcard</title>
<link href="https://fonts.googleapis.com/css2?family=Anton&family=Nunito:wght@700;800&family=Cabin:wght@400&family=Roboto:wght@400;700&family=Roboto+Condensed:ital,wght@1,700&display=swap" rel="stylesheet">
<style>
  :root {
    --blue: #1c8fd9;
    --pink: #e11b5b;
    --yellow: #f2e21c;
    --green: #6cbb2e;
    --ink: #222222;
    --paper: #ffffff;
    --light: #f1f1f1;
    --stamp: #e2e2e2;
    --page: #e9e9e7;
  }
  * { margin: 0; padding: 0; box-sizing: border-box; }
  html, body { width: 1200px; height: 900px; overflow: hidden; background: var(--page); }
  .canvas { position: relative; width: 1200px; height: 900px; }

  .postcard {
    position: absolute; left: 280px; width: 692px; height: 460px;
    transform: scale(0.925); transform-origin: top left;
    overflow: hidden; box-shadow: 0 4px 14px rgba(0,0,0,.18);
  }
  .postcard--back { top: 16px; background: var(--paper); }
  .postcard--front { top: 458px; background: var(--light); }
  .postcard svg.bg { position: absolute; inset: 0; }
  .abs { position: absolute; }

  /* shared brand name */
  .brand-mark { border-radius: 50%; background: var(--green); }
  .brand-name {
    font-family: "Nunito", sans-serif; font-weight: 800; color: var(--green);
    text-align: center; line-height: 1.05;
  }

  /* call pills */
  .call-tag {
    background: var(--yellow); border-radius: 10px;
    font-family: "Roboto Condensed", sans-serif; font-style: italic; font-weight: 700;
    color: var(--ink); text-align: center;
  }
  .phone-pill {
    background: var(--pink); border: 3px solid var(--paper); border-radius: 30px;
    box-shadow: 0 2px 4px rgba(0,0,0,.25);
    font-family: "Roboto", sans-serif; font-weight: 700; color: var(--paper);
    text-align: right; letter-spacing: .5px;
  }
  .phone-icon {
    border-radius: 50%; background: var(--pink); border: 3px solid var(--paper);
    display: flex; align-items: center; justify-content: center;
  }

  /* back */
  .back-logo-mark { left: 157px; top: 38px; width: 56px; height: 56px; }
  .back-brand { left: 20px; top: 128px; width: 330px; font-size: 28px; }
  .back-copy { font-family: "Roboto", sans-serif; font-size: 11px; line-height: 13px; color: var(--ink); width: 250px; left: 58px; }
  .back-copy .hl { color: var(--green); }
  .back-headline {
    left: 60px; top: 284px; width: 258px; text-align: right;
    font-family: "Roboto", sans-serif; font-weight: 700; font-size: 19px; line-height: 25px; color: var(--blue);
  }
  .back-headline .hl { color: var(--pink); }
  .stamp-box { left: 585px; top: 9px; width: 97px; height: 95px; background: var(--stamp); outline: 2px dashed #f7f7f7; outline-offset: -3px; }

  /* front */
  .front-title {
    left: 0; top: 30px; width: 440px; text-align: center;
    font-family: "Anton", sans-serif; color: var(--paper); font-size: 84px; line-height: 84px; letter-spacing: 2px;
  }
  .front-sub { left: 0; top: 212px; width: 380px; text-align: center; font-family: "Nunito", sans-serif; font-weight: 800; font-size: 32px; color: var(--yellow); }
  .front-copy { left: 20px; top: 270px; width: 330px; text-align: center; font-family: "Cabin", sans-serif; font-size: 16px; line-height: 21px; color: var(--paper); }
  .child-art {
    left: 340px; top: 182px; width: 215px; height: 278px;
    border-radius: 100px 100px 0 0;
    background: linear-gradient(180deg, #5a3a26 0%, #a8643f 45%, #2fa3c9 78%, #c2492f 100%);
  }
  .front-logo-mark { left: 541px; top: 40px; width: 56px; height: 56px; }
  .front-brand { left: 470px; top: 116px; width: 200px; font-size: 25px; }
  .free-badge {
    left: 521px; top: 193px; width: 128px; height: 128px; border-radius: 50%; background: var(--yellow);
    text-align: center; padding-top: 18px; font-family: "Roboto Condensed", sans-serif; font-style: italic; font-weight: 700; color: var(--pink);
  }
  .free-badge .lead { font-family: "Roboto", sans-serif; font-style: normal; font-size: 19px; color: var(--ink); line-height: 22px; }
  .free-badge .big { font-size: 38px; line-height: 36px; }
  .free-badge .small { font-size: 25px; line-height: 26px; }
  .social-badge { top: 384px; width: 37px; height: 37px; border-radius: 4px; }
  .social-badge--one { left: 567px; background: #3a5a98; }
  .social-badge--two { left: 617px; background: #d43d7a; }
</style>
</head>
<body>
<main class="canvas">

  <!-- Reverse side -->
  <section class="postcard postcard--back">
    <svg class="bg" width="692" height="460" viewBox="0 0 692 460">
      <rect width="692" height="460" fill="var(--blue)"/>
      <path d="M100 0 H692 V460 H330 C150 440 25 360 25 200 C25 110 60 40 100 0 Z" fill="var(--paper)" stroke="var(--yellow)" stroke-width="7"/>
    </svg>
    <div class="abs stamp-box"></div>
    <div class="abs brand-mark back-logo-mark"></div>
    <div class="abs brand-name back-brand">Bright Lantern Youth</div>
    <p class="abs back-copy" style="top:183px"><span class="hl">Bright Lantern Youth</span> is a nonprofit organization providing meals and medical services to children in need across Honduras.</p>
    <p class="abs back-copy" style="top:234px;width:240px">Your gently used clothing can fund life - changing programs and provide hope to those who need it most.</p>
    <p class="abs back-headline">Give the <span class="hl">gift of care today</span><br>your donation makes<br>a difference!</p>
    <div class="abs call-tag" style="left:112px;top:371px;width:210px;height:19px;font-size:13px;line-height:19px">Call us to schedule your pickup</div>
    <div class="abs phone-pill" style="left:78px;top:390px;width:268px;height:46px;font-size:30px;line-height:40px;padding-right:14px">555-014-2736</div>
    <div class="abs phone-icon" style="left:46px;top:389px;width:48px;height:48px">
      <svg width="24" height="24" viewBox="0 0 24 24"><path d="M6.6 10.8c1.4 2.8 3.8 5.1 6.6 6.6l2.2-2.2c.3-.3.7-.4 1-.2 1.1.4 2.3.6 3.6.6.6 0 1 .4 1 1V20c0 .6-.4 1-1 1C10.6 21 3 13.4 3 4c0-.6.4-1 1-1h3.5c.6 0 1 .4 1 1 0 1.3.2 2.5.6 3.6.1.3 0 .7-.2 1l-2.3 2.2z" fill="var(--paper)"/></svg>
    </div>
  </section>

  <!-- Front side -->
  <section class="postcard postcard--front">
    <svg class="bg" width="692" height="460" viewBox="0 0 692 460">
      <path d="M0 0 H382 C430 60 455 140 455 240 V460 H0 Z" fill="var(--blue)"/>
    </svg>
    <h1 class="abs front-title">DONATE<br>CLOTHING</h1>
    <p class="abs front-sub">Change Lives!</p>
    <p class="abs front-copy">Your gently used clothing can fund<br>life-changing programs and provide hope<br>to those who need it most.</p>
    <div class="abs child-art" role="img" aria-label="Illustration of a smiling child with curly hair, a teal shirt and a red backpack"></div>
    <div class="abs call-tag" style="left:92px;top:362px;width:232px;height:20px;font-size:14px;line-height:20px">Call us to schedule your pickup</div>
    <div class="abs phone-pill" style="left:56px;top:380px;width:294px;height:52px;font-size:34px;line-height:46px;padding-right:16px">555-014-2736</div>
    <div class="abs phone-icon" style="left:20px;top:379px;width:54px;height:54px">
      <svg width="26" height="26" viewBox="0 0 24 24"><path d="M6.6 10.8c1.4 2.8 3.8 5.1 6.6 6.6l2.2-2.2c.3-.3.7-.4 1-.2 1.1.4 2.3.6 3.6.6.6 0 1 .4 1 1V20c0 .6-.4 1-1 1C10.6 21 3 13.4 3 4c0-.6.4-1 1-1h3.5c.6 0 1 .4 1 1 0 1.3.2 2.5.6 3.6.1.3 0 .7-.2 1l-2.3 2.2z" fill="var(--paper)"/></svg>
    </div>
    <div class="abs brand-mark front-logo-mark"></div>
    <div class="abs brand-name front-brand">Bright Lantern<br>Youth</div>
    <div class="abs free-badge">
      <div class="lead">We offer</div>
      <div class="big">FREE</div>
      <div class="small">Pickups</div>
    </div>
    <div class="abs social-badge social-badge--one"></div>
    <div class="abs social-badge social-badge--two"></div>
  </section>

</main>
</body>
</html>
```